Copperfen Hollow Wine And Spirits

We need to design a website for our Liquor Store

Industry/Entity Type

Store

Number of Pages Required

4 page

Requirements
Must have
• Beer, Liquor, Wine & Cigar related theme.
• Mention our 8-locations addresses & maps info
Nice to have
• category for Beer, Liquor & Wine to setup database for item list to link our sql server database.

```html
<!DOCTYPE html>
<html lang="en">
<head>
<meta charset="utf-8">
<title>Copperfen Hollow Wine And Spirits</title>
<link rel="stylesheet" href="https://fonts.googleapis.com/css2?family=Cormorant+Garamond:wght@600;700&family=Montserrat:wght@400;600;700&family=Open+Sans:wght@400;600&display=swap">
<style>
:root{
  --green:#18220f;
  --green-deep:#101a0b;
  --footer:#0d1509;
  --black:#050505;
  --gold:#b98f2b;
  --gold-soft:#c9a44a;
  --light:#f4f4f4;
  --white:#ffffff;
  --text:#333333;
  --muted:#9a9a9a;
  --serif:'Cormorant Garamond', Georgia, serif;
  --caps:'Montserrat', Arial, sans-serif;
  --body:'Open Sans', Arial, sans-serif;
}
*{box-sizing:border-box;margin:0;padding:0}
html,body{width:1200px;height:4009px;overflow:hidden}
body{position:relative;background:var(--light);font-family:var(--body);color:var(--text)}
section,header,footer{position:absolute;left:0;width:1200px}
.abs{position:absolute}
.btn-outline{position:absolute;border:2px solid var(--gold);color:var(--white);font:600 12px var(--caps);letter-spacing:3px;text-transform:uppercase;display:flex;align-items:center;justify-content:center}
.btn-solid{position:absolute;background:var(--gold);color:var(--white);font:600 13px var(--caps);letter-spacing:3px;text-transform:uppercase;display:flex;align-items:center;justify-content:center}
.section-title{position:absolute;left:0;width:1200px;text-align:center;font:700 38px var(--serif);color:var(--text)}
.section-sub{position:absolute;left:0;width:1200px;text-align:center;font:600 17px var(--caps);letter-spacing:7px;color:var(--gold);text-transform:uppercase}

/* hero */
.hero{top:0;height:575px;background:linear-gradient(100deg,#2b1a0e 0%,#4a2e17 35%,#3a2311 60%,#1d120a 100%)}
.hero-photo{position:absolute;inset:0;background:radial-gradient(ellipse at 85% 60%,rgba(225,220,205,.35),transparent 40%),linear-gradient(180deg,rgba(0,0,0,.25),rgba(0,0,0,.1))}
.brand{position:absolute;left:85px;top:46px;width:140px;font:700 24px/1 var(--serif);color:var(--white)}
.nav{position:absolute;left:267px;top:74px;display:flex;gap:40px;list-style:none}
.nav li{font:700 12px var(--caps);color:var(--white);letter-spacing:1px;text-transform:uppercase}
.search{position:absolute;left:1084px;top:70px}
.hero-title{position:absolute;left:140px;top:208px;font:700 50px/1 var(--serif);color:var(--white)}
.hero-title span{display:block;font-size:42px;margin-top:4px}
.hero-text{position:absolute;left:142px;top:318px;width:380px;font:400 14px/1.6 var(--body);color:#e8e2d8}

/* welcome */
.welcome{top:575px;height:382px;background:var(--green)}
.welcome .section-title{top:66px;color:var(--white);font-size:40px}
.ampline{position:absolute;left:0;width:1200px;top:120px;display:flex;justify-content:center;align-items:center;gap:18px;font:400 18px var(--caps);letter-spacing:9px;color:var(--gold)}
.ampline b{font:700 70px/1 var(--serif);color:var(--gold);letter-spacing:0}
.welcome-text{position:absolute;left:140px;top:198px;width:920px;text-align:center;font:400 11px/1.75 var(--body);color:#6f7666}

/* best sellers */
.best{top:957px;height:647px;background:var(--light)}
.best .section-title{top:58px}
.best .section-sub{top:108px}
.cat-list{position:absolute;left:85px;top:290px;list-style:none}
.cat-list li{font:600 13px/26px var(--caps);letter-spacing:4px;color:var(--gold-soft);text-transform:uppercase}
.cat-list li.active{color:var(--gold);font-weight:700}
.bottles{position:absolute;left:415px;top:165px;width:347px;height:348px;background:linear-gradient(90deg,#e9e6dd 0%,#d9d3c2 30%,#2a1618 50%,#d8cfc8 70%,#ebe8e4 100%);border-radius:6px;opacity:.9}
.feature{position:absolute;left:829px;top:280px;width:280px}
.feature h3{font:700 20px var(--serif);color:var(--text);margin-bottom:12px}
.feature p{font:400 12px/1.75 var(--body);color:var(--muted)}
.pager{position:absolute;top:550px;font:600 11px var(--caps);letter-spacing:4px;color:var(--text)}

/* selection */
.selection{top:1604px;height:989px;background:var(--light)}
.selection .section-title{top:52px}
.selection .section-sub{top:112px}
.selection-text{position:absolute;left:85px;top:160px;width:1030px;text-align:center;font:400 12px/1.75 var(--body);color:#444}
.tab{position:absolute;top:272px;width:134px;height:43px;border:2px solid var(--gold);font:700 12px var(--caps);letter-spacing:3px;color:var(--text);display:flex;align-items:center;justify-content:center;text-transform:uppercase;background:var(--white)}
.tab.active{background:var(--gold);color:var(--white)}
.card{position:absolute;width:289px;height:254px;background:var(--white);display:flex;align-items:center;justify-content:center}
.card .bottle{width:70px;height:170px;border-radius:8px}
.card.featured{background:var(--green)}
.card.featured h4{font:700 26px var(--serif);color:var(--white);margin-bottom:14px;text-align:center}
.card.featured .btn-solid{position:relative;width:194px;height:36px;font-size:12px}

/* promo */
.promo{top:2593px;height:294px;background:linear-gradient(90deg,#4a2a0a 0%,#7a4f16 25%,#a36c1f 45%,#6e4412 70%,#3a1f08 100%)}
.promo-title{position:absolute;left:235px;top:100px;font:700 36px var(--serif);color:var(--white)}
.promo-sub{position:absolute;left:237px;top:148px;font:700 15px var(--caps);letter-spacing:5px;color:var(--white)}
.promo-lettering{position:absolute;left:745px;top:55px;width:175px;height:130px;background:rgba(255,255,255,.18);border-radius:8px}

/* location */
.location{top:2887px;height:641px;background:var(--light)}
.location .section-title{top:48px}
.location .section-sub{top:104px}
.branch-list{position:absolute;left:85px;top:246px;list-style:none}
.branch-list li{font:600 13px/28px var(--caps);letter-spacing:4px;color:var(--gold-soft);text-transform:uppercase}
.branch-list li.active{color:var(--gold);font-weight:700}
.map{position:absolute;left:350px;top:187px;width:345px;height:393px;background:linear-gradient(135deg,#efe8d8 0%,#e6e3dc 50%,#dcdfe3 100%)}
.address{position:absolute;left:722px;top:250px;width:300px}
.address h4{font:700 14px var(--body);color:var(--text);display:flex;align-items:center;gap:8px}
.address .lines{margin:10px 0 0 22px;font:400 12px/1.8 var(--body);color:#555}
.address p.desc{margin:22px 0 0 22px;font:400 12px/1.75 var(--body);color:var(--muted)}
.location .btn-outline{left:727px;top:468px;width:217px;height:35px;color:var(--gold);font-size:11px}

/* footer */
.site-footer{top:3528px;height:407px;background:var(--footer)}
.foot-col{position:absolute;top:92px}
.foot-col h5{font:700 15px var(--caps);letter-spacing:2px;color:var(--gold);text-transform:uppercase;margin-bottom:18px}
.foot-about{left:85px;top:100px;width:230px;font:400 12px/1.75 var(--body);color:#7c8474}
.foot-about a{display:block;margin-top:16px;color:var(--gold);text-decoration:none}
.quick{left:358px}
.quick ul{list-style:none}
.quick li{font:400 13px/37px var(--body);color:var(--white)}
.quick li.active{color:var(--gold)}
.news{left:612px;width:260px}
.news-item{display:flex;gap:14px;margin-bottom:42px}
.news-thumb{width:43px;height:43px;flex:none;background:linear-gradient(135deg,#8a8f94,#4b5057)}
.news-thumb.plus{background:var(--gold);display:flex;align-items:center;justify-content:center}
.news-item p{font:400 12px/1.55 var(--body);color:var(--white)}
.news-item b{font:700 12px var(--caps);letter-spacing:1px;display:block}
.news-item small{display:block;font-size:11px;margin-top:2px}
.letter{left:911px}
.letter-form{display:flex;width:201px;height:32px}
.letter-form span{flex:1;background:#2a2f27;color:#ccc;font:400 12px var(--body);display:flex;align-items:center;padding-left:12px}
.letter-form i{width:32px;background:var(--gold);display:flex;align-items:center;justify-content:center}
.social-head{font:700 14px var(--caps);letter-spacing:2px;color:var(--white);margin:28px 0 10px}
.social{display:flex;gap:8px}
.social span{width:30px;height:30px;border-radius:50%;background:var(--white)}
.copy{position:absolute;left:0;top:3935px;width:1200px;height:74px;background:var(--black);color:#cfcfcf;font:400 12px var(--body);display:flex;align-items:center;justify-content:center}
</style>
</head>
<body>

<header class="hero">
  <div class="hero-photo" role="img" aria-label="Dark wooden table with a whisky bottle and glasses"></div>
  <div class="brand">Copperfen Hollow</div>
  <ul class="nav">
    <li>Home</li><li>Our Location</li><li>Products</li><li>About Us</li><li>Contact Us</li>
  </ul>
  <svg class="search" width="22" height="22" viewBox="0 0 22 22" fill="none" stroke="#fff" stroke-width="3"><circle cx="9" cy="9" r="6.5"/><path d="M14 14l6 6" stroke-linecap="round"/></svg>
  <h1 class="hero-title">Reprehenderit<span>voluptate</span></h1>
  <p class="hero-text">Excepteur sint occaecat cupidatat non proident, sunt in culpa qui officia deserunt mollit anim id est laborum.</p>
  <div class="btn-outline" style="left:147px;top:396px;width:160px;height:36px">Learn More</div>
</header>

<section class="welcome">
  <h2 class="section-title">Welcome to Copperfen Hollow</h2>
  <div class="ampline"><span>WINES</span><b>&amp;</b><span>SPIRITS</span></div>
  <p class="welcome-text">Lorem ipsum dolor sit amet, consectetur adipiscing elit, sed do eiusmod tempor incididunt ut labore et dolore magna aliqua. Ut enim ad minim veniam, quis nostrud exercitation ullamco laboris nisi ut aliquip ex ea commodo consequat. Lorem ipsum dolor sit amet, consectetur adipiscing elit, sed do eiusmod tempor incididunt ut labore et dolore magna aliqua. Ut enim ad minim veniam, quis nostrud exercitation ullamco laboris nisi ut aliquip ex ea commodo consequat.</p>
  <div class="btn-outline" style="left:520px;top:291px;width:160px;height:36px">Learn More</div>
</section>

<section class="best">
  <h2 class="section-title">Our Best</h2>
  <div class="section-sub">Sellers</div>
  <ul class="cat-list">
    <li class="active">Wines</li><li>Spirits</li><li>Beer</li><li>Cigar</li>
  </ul>
  <div class="bottles" role="img" aria-label="Row of wine and champagne bottles with a red wine bottle in front"></div>
  <div class="feature">
    <h3>Harrowgate Red Wine</h3>
    <p>Duis aute irure dolor in reprehenderit in voluptate velit esse cillum dolore eu fugiat nulla pariatur. Excepteur sint occaecat cupidatat non proident, sunt in culpa qui officia deserunt mollit anim id est laborum.</p>
  </div>
  <svg class="abs" style="left:495px;top:550px" width="60" height="10" viewBox="0 0 60 10"><path d="M2 5h56M2 5l5-4M2 5l5 4" stroke="#222" stroke-width="2" fill="none"/></svg>
  <svg class="abs" style="left:652px;top:550px" width="60" height="10" viewBox="0 0 60 10"><path d="M2 5h56M58 5l-5-4M58 5l-5 4" stroke="#222" stroke-width="2" fill="none"/></svg>
  <div class="pager" style="left:502px;top:572px">Prev</div>
  <div class="pager" style="left:657px;top:572px">Next</div>
</section>

<section class="selection">
  <h2 class="section-title">Our Selection</h2>
  <div class="section-sub">Check These Out</div>
  <p class="selection-text">Lorem ipsum dolor sit amet, consectetur adipiscing elit, sed do eiusmod tempor incididunt ut labore et dolore magna aliqua. Ut enim ad minim veniam, quis nostrud exercitation ullamco laboris nisi ut aliquip ex ea commodo consequat. Lorem ipsum dolor sit amet, consectetur adipiscing elit, sed do eiusmod tempor incididunt ut labore et dolore magna aliqua. Ut enim ad minim veniam, quis nostrud exercitation ullamco laboris nisi ut aliquip ex ea commodo consequat.</p>
  <div class="tab active" style="left:307px">Wines</div>
  <div class="tab" style="left:457px">Spirits</div>
  <div class="tab" style="left:609px">Beer</div>
  <div class="tab" style="left:759px">Cigar</div>

  <div class="card" style="left:142px;top:382px"><div class="bottle" role="img" aria-label="Bourbon bottle" style="width:80px;height:160px;background:linear-gradient(180deg,#3a2a1a 0%,#b8661c 40%,#8a3f10 100%)"></div></div>
  <div class="card" style="left:454px;top:382px"><div class="bottle" role="img" aria-label="Cognac bottle" style="width:85px;height:170px;background:linear-gradient(180deg,#c8a25a 0%,#d0621e 45%,#8f3a0d 100%)"></div></div>
  <div class="card" style="left:767px;top:382px"><div class="bottle" role="img" aria-label="White wine bottle" style="width:55px;height:190px;background:linear-gradient(180deg,#c9b23a 0%,#e9dc8a 50%,#d9c865 100%)"></div></div>
  <div class="card" style="left:142px;top:660px"><div class="bottle" role="img" aria-label="Red wine bottle" style="width:55px;height:200px;background:linear-gradient(180deg,#1a1414 0%,#2a1f1a 55%,#d9cfb0 70%,#1a1414 85%)"></div></div>
  <div class="card featured" style="left:454px;top:660px"><div><h4>Maison Verlaine</h4><div class="btn-solid">More Details</div></div></div>
  <div class="card" style="left:767px;top:660px"><div class="bottle" role="img" aria-label="Red wine bottle" style="width:55px;height:200px;background:linear-gradient(180deg,#5a1218 0%,#2a0c10 50%,#e5dccb 65%,#2a0c10 85%)"></div></div>
</section>

<section class="promo" role="img" aria-label="Blurred close-up of bottle necks in warm light">
  <h2 class="promo-title">Season of Sharing</h2>
  <div class="promo-sub">GET THE BEST DEAL</div>
  <div class="promo-lettering" role="img" aria-label="Hand lettered offer: Buy One Get Two"></div>
  <div class="btn-solid" style="left:740px;top:208px;width:193px;height:35px;font-size:12px">Read More</div>
</section>

<section class="location">
  <h2 class="section-title">Our Location</h2>
  <div class="section-sub">Find a Branch Near You</div>
  <ul class="branch-list">
    <li class="active">Inventore</li><li>Verit</li><li>Architecto</li><li>Explicabo</li><li>Voluptatem</li><li>Exercitationem</li><li>Suscipit</li><li>Commodi</li>
  </ul>
  <div class="map" role="img" aria-label="Street map of the selected branch with a location marker"></div>
  <div class="address">
    <h4><svg width="14" height="18" viewBox="0 0 14 18"><path d="M7 0a7 7 0 0 0-7 7c0 5 7 11 7 11s7-6 7-11a7 7 0 0 0-7-7z" fill="#222"/><circle cx="7" cy="7" r="2.5" fill="#f4f4f4"/></svg>Inventore, Albrestus</h4>
    <div class="lines">143 Duis st. Cor Irure Dolor.<br>(02) 555 0142</div>
    <p class="desc">Duis aute irure dolor in reprehenderit in voluptate velit esse cillum dolore eu fugiat nulla pariatur. Excepteur sint occaecat cupidatat non proident, sunt in culpa qui officia deserunt mollit anim id est laborum commodo consequat. Lorem ipsum dolor sit amet.</p>
  </div>
  <div class="btn-outline">How to Get Here</div>
</section>

<footer class="site-footer">
  <p class="foot-col foot-about">Vivamus viverra, ligula non tincidunt pulvinar, augue est sagittis leo, id feugiat enim lorem quis nisl. Quisque ac arcu egestas, convallis risus vitae, gravida enim.<a>Read More</a></p>
  <div class="foot-col quick">
    <h5>Quick Links</h5>
    <ul><li>Home</li><li class="active">About Us</li><li>Services</li><li>Products</li><li>Location</li></ul>
  </div>
  <div class="foot-col news">
    <h5>Latest News</h5>
    <div class="news-item"><div class="news-thumb" role="img" aria-label="News photo"></div><p><b>LOREM IPSUM</b>Phasellus ut condimentum diam, eget tempus lorem.<small>21 December, 2017</small></p></div>
    <div class="news-item"><div class="news-thumb plus"><svg width="18" height="18" viewBox="0 0 18 18"><path d="M9 2v14M2 9h14" stroke="#fff" stroke-width="3"/></svg></div><p><b>LOREM IPSUM</b>Phasellus ut condimentum diam, eget tempus lorem.<small>21 December, 2017</small></p></div>
  </div>
  <div class="foot-col letter">
    <h5>News Letter</h5>
    <div class="letter-form"><span>Your email here</span><i><svg width="12" height="12" viewBox="0 0 12 12"><path d="M1 6h9M6 2l4 4-4 4" stroke="#fff" stroke-width="2" fill="none"/></svg></i></div>
    <div class="social-head">SOCIAL</div>
    <div class="social"><span></span><span></span><span></span></div>
  </div>
</footer>
<div class="copy">Copperfen Hollow Copyright 2017</div>

</body>
</html>
```